Two (Similar) Posters - Both 11" x 17"

We are looking for two posters - both 11" x 17" (vertical orientation) - to promote two consecutive, cardiology-related events:

Poster #1) The Inaugural New York ROC Brainbuzz Competition, Cocktail Reception and Whiskey Tasting (http://hb-pvl.org/brainbuzz-and-reception)

and

Poster #2) The 89th Annual Scientific Session and 27th Annual Meeting (http://hb-pvl.org/2017annualmtg)

#1 is a cocktail party with a whiskey tasting that will also feature a gameshow-like event with the med students, and #2 is an educational conference for doctors

Target Market(s)

Healthcare providers (Please do not include stock images of medical professionals; in fact, please use caution with any stock imagery, as it most likely will not be appropriate.)

Industry/Entity Type

Education

Colors

Designer to choose colors to be used in the design.

Requirements
Must have
• Each poster design should include:
• - the 4 logos of the participating organizations (I can upload various other versions if needed) along with the "wording" that goes alongside each one (see "STD_small" image as an example)
• - name of event
• - date, time and location
• - where to register
• - where to get more information
• - some artistic flavor or detailing
• Final (raw) files in an .ai, .psd, .eps or .idml format are required upon project completion.
Nice to have
• It's not crucial that these two posters "match," but it would be nice if they at least coordinated with each other. Would be nice if the designer could stay close to our color scheme (can be found here - http://hb-pvl.org/), but this isn't crucial. Posters should be upscale, neat and professional.
Should not have
• Should not be too difficult to read. These are posters that will likely be hanging on a bulletin board in hospital staff break rooms. Should not be too cartoon-like or silly. The two should not look EXACTLY the same in case people think that they are the same poster.

```html
<!DOCTYPE html>
<html lang="en">
<head>
<meta charset="utf-8">
<title>Event Posters – Brainbuzz Reception &amp; Annual Scientific Session</title>
<link rel="stylesheet" href="https://fonts.googleapis.com/css2?family=Cinzel:wght@400;600&display=swap">
<style>
  :root {
    --navy: #1c3667;
    --navy-deep: #13295a;
    --navy-light: #2a4c86;
    --paper: #eceef1;
    --paper-shade: #dcdfe5;
    --ink: #2a4677;
    --white: #ffffff;
    --wood: #6b4527;
    --amber: #c48a4a;
    --stone: #8a7e6c;
    --gold: #b79a5e;
  }
  * { box-sizing: border-box; margin: 0; padding: 0; }
  html, body { width: 1200px; height: 926px; overflow: hidden; background: var(--white); }
  body { position: relative; font-family: "Cinzel", "Times New Roman", serif; }

  .poster { position: absolute; top: 0; height: 926px; text-align: center; }
  .poster--reception { left: 0; width: 600px; background: var(--navy); }
  .poster--session { left: 608px; width: 592px; background: var(--white); }

  .sheet { position: absolute; left: 10px; top: 10px; width: 580px; height: 818px;
    background: linear-gradient(160deg, var(--paper) 0%, #f4f5f7 45%, var(--paper-shade) 100%); color: var(--ink); }
  .field { position: absolute; left: 0; top: 0; width: 592px; height: 828px;
    background: linear-gradient(170deg, var(--navy-light) 0%, var(--navy) 45%, var(--navy-deep) 100%); color: var(--white); }

  .block { position: absolute; left: 0; width: 100%; }
  .headline { font-size: 38px; font-weight: 400; letter-spacing: 2px; line-height: 1; }
  .event-title { font-size: 19px; line-height: 23px; letter-spacing: .5px; }
  .detail { font-size: 16px; line-height: 20px; letter-spacing: .4px; }
  .register { font-size: 15.5px; letter-spacing: .5px; }
  .info { font-size: 13px; line-height: 16px; letter-spacing: .4px; }
  .summary { font-size: 12.4px; line-height: 15.4px; letter-spacing: .3px; left: 36px; width: 520px; }

  .photos { position: absolute; left: 0; }
  .photos svg { display: block; }

  .partners { position: absolute; left: 0; top: 828px; width: 100%; height: 98px;
    display: flex; align-items: center; justify-content: space-between; padding: 0 16px; }
  .poster--reception .partners { color: var(--white); }
  .poster--session .partners { color: var(--navy); }
  .partner { display: flex; align-items: center; gap: 6px; text-align: left; width: 138px; }
  .partner-mark { flex: none; width: 52px; height: 52px; border-radius: 50%; border: 2px solid currentColor; }
  .partner-name { font-size: 7.4px; line-height: 9px; letter-spacing: .2px; }
</style>
</head>
<body>

<section class="poster poster--reception">
  <div class="sheet">
    <h1 class="block headline" style="top:30px">Come and Join Us</h1>
    <p class="block event-title" style="top:110px">The Inaugural New York<br>ROC Brainbuzz Competition,<br>Cocktail Reception &amp; Whiskey Tasting</p>
    <p class="block detail" style="top:204px">Oak &amp; Ember, 14 W 39th St, New York, NY 10018</p>
    <p class="block detail" style="top:238px">Wednesday, Dec. 6th, 2017,<br>from 6:30 p.m. to 10:30 p.m.</p>
    <p class="block detail" style="top:296px">Free for HBCS/ACoC Members<br>and $30 for nonmembers and guests</p>
    <p class="block register" style="top:356px">Register online at hb-pvl.org/2017annualmtg</p>

    <div class="photos" style="top:386px">
      <svg width="580" height="348" viewBox="0 0 580 348">
        <defs>
          <linearGradient id="venueA" x1="0" y1="0" x2="0" y2="1">
            <stop offset="0" stop-color="#4a3020"/><stop offset=".55" stop-color="#8a5a34"/><stop offset="1" stop-color="#c9b8a0"/>
          </linearGradient>
          <linearGradient id="venueB" x1="0" y1="0" x2="1" y2="1">
            <stop offset="0" stop-color="#3a2a22"/><stop offset=".5" stop-color="#a06a3c"/><stop offset="1" stop-color="#d8cdbd"/>
          </linearGradient>
          <linearGradient id="venueC" x1="0" y1="0" x2="0" y2="1">
            <stop offset="0" stop-color="#6e6658"/><stop offset=".6" stop-color="#8a7a66"/><stop offset="1" stop-color="#4c3a2c"/>
          </linearGradient>
        </defs>
        <polygon points="0,106 178,32 178,348 0,348" fill="url(#venueA)" role="img" aria-label="Venue lounge with carved fireplace and candlelit tables"/>
        <polygon points="188,28 374,28 374,348 188,348" fill="url(#venueB)" role="img" aria-label="Venue dining room with globe pendant lights and whiskey shelves"/>
        <polygon points="384,32 580,106 580,348 384,348" fill="url(#venueC)" role="img" aria-label="Venue parlor with marble fireplace and framed painting"/>
      </svg>
    </div>

    <p class="block info" style="top:752px">For more information or<br>to inquire about becoming an exhibitor,<br>call (212) 555-0147 or email ask@hb-pvl.org</p>
  </div>

  <footer class="partners">
    <div class="partner"><span class="partner-mark"></span><span class="partner-name">Presented by<br>The Hudson Bay Cardiac Society, Inc.</span></div>
    <div class="partner"><span class="partner-mark"></span><span class="partner-name">Of the<br>Empire State Chapter, Allied College of Cardiology</span></div>
    <div class="partner"><span class="partner-mark"></span><span class="partner-name">In association with<br>Metro Heart Center</span></div>
    <div class="partner"><span class="partner-mark"></span><span class="partner-name">And<br>Hudson – Andes Chapter Exchange Program</span></div>
  </footer>
</section>

<section class="poster poster--session">
  <div class="field">
    <h1 class="block headline" style="top:42px">Save the Date</h1>
    <p class="block event-title" style="top:124px">The 89th Annual Scientific Session &amp;<br>27th Annual Meeting</p>
    <p class="block detail" style="top:190px">The Regent Hall Ballroom,<br>22 E. 29th St., New York, NY</p>
    <p class="block detail" style="top:244px">Thursday, Dec. 7th, 2017,<br>from 7:30 a.m. to 3 p.m.</p>

    <div class="photos" style="top:300px">
      <svg width="592" height="216" viewBox="0 0 592 216">
        <defs>
          <linearGradient id="hallA" x1="0" y1="0" x2="0" y2="1">
            <stop offset="0" stop-color="#4a3222"/><stop offset=".5" stop-color="#a8723e"/><stop offset="1" stop-color="#d2c4b0"/>
          </linearGradient>
          <linearGradient id="hallB" x1="0" y1="0" x2="0" y2="1">
            <stop offset="0" stop-color="#6a4a30"/><stop offset=".45" stop-color="#c49658"/><stop offset="1" stop-color="#8a8c96"/>
          </linearGradient>
          <linearGradient id="hallC" x1="0" y1="0" x2="1" y2="1">
            <stop offset="0" stop-color="#d8d6d0"/><stop offset=".5" stop-color="#8a8680"/><stop offset="1" stop-color="#3a3a3c"/>
          </linearGradient>
        </defs>
        <polygon points="0,0 165,0 135,216 0,216" fill="url(#hallA)" role="img" aria-label="Candlelit lounge seating area"/>
        <polygon points="175,0 420,0 390,216 145,216" fill="url(#hallB)" role="img" aria-label="Grand ballroom with ornate gilded ceiling and columns"/>
        <polygon points="430,0 592,0 592,216 400,216" fill="url(#hallC)" role="img" aria-label="Modern bar with stools and backlit shelves"/>
      </svg>
    </div>

    <p class="block summary" style="top:548px">The Annual Scientific Session brings together cardiologists, cardia-thoracic surgeons, internists, family practitioners, gerontologists, oncologists, cardiac nurse practitioners, physician assistants, cardiology fellows in training (ROCs) and all members of the cardiac care team, and, this year, will feature the winners of the Annual Young Investigators' Competition for case studies and abstracts (posters), which is now open!</p>
    <p class="block register" style="top:712px">Register online at hb-pvl.org/2017annualmtg</p>
    <p class="block info" style="top:756px">For more information or<br>to inquire about becoming an exhibitor,<br>call (212) 555-0147 or email ask@hb-pvl.org</p>
  </div>

  <footer class="partners">
    <div class="partner"><span class="partner-mark"></span><span class="partner-name">Presented by<br>The Hudson Bay Cardiac Society, Inc.</span></div>
    <div class="partner"><span class="partner-mark"></span><span class="partner-name">Of the<br>Empire State Chapter, Allied College of Cardiology</span></div>
    <div class="partner"><span class="partner-mark"></span><span class="partner-name">In association with<br>Metro Heart Center</span></div>
    <div class="partner"><span class="partner-mark"></span><span class="partner-name">And<br>Hudson – Andes Chapter Exchange Program</span></div>
  </footer>
</section>

</body>
</html>
```